GLP letterhead

We need a letterhead design for our new company based in Los Angeles called "Gold Lantern Pictures". We develop film and television projects. We work with investors, financiers, film production companies, film distribution and sales companies as well as studios. We would like to incorporate our logo (see attached) but make the letterhead simple and elegant. We need to include: logo, company address, phone number and company website.
Updates

Hello designers, Thanks for your submissions. For our letterhead, we are looking for something more simple and elegant. No heavy bars or lines. Make it feel light and clean. Not a lot of ink on the page. Use the logo and contact info but think "clean", "streamlined" and mostly white paper. Looking forward to seeing more... thanks! Gold Lantern Pictures team

Target Market(s)

Studio executives, talent agents and agencies, financiers, investors.

Industry/Entity Type

It Company

Requirements
Must have
• Gold Lantern Pictures logo (see attached). Logo may be cropped and altered appropriately for elegant letterhead design.
• Please include:
• COMPANY ADDRESS:
• Ridgeway Studio Park
• 2850 Halverson Street
• Tower Annex, 4th Floor
• Manhattan Beach, CA 90412
• COMPANY WEBSITE:
• www.goldlanternpicturesco.example
• COMPANY PHONE NUMBER:
• 310-555-0148

```html
<!DOCTYPE html>
<html lang="en">
<head>
<meta charset="utf-8">
<title>Gold Lantern Pictures — Stationery</title>
<link rel="stylesheet" href="https://fonts.googleapis.com/css2?family=Exo+2:wght@400;600;700&display=swap">
<style>
  :root {
    --board: #ebebeb;
    --paper: #ffffff;
    --ink: #231f20;
    --ink-soft: #55585e;
    --hairline: #d9dde3;
    --accent: #1b7fd0;
    --accent-light: #a9c6ea;
    --accent-wash: #f1f6fc;
    --logo-blue: #1ea7e0;
    --shadow: 2px 3px 6px rgba(0,0,0,0.28);
  }
  * { box-sizing: border-box; margin: 0; padding: 0; }
  html, body { width: 1200px; height: 1000px; overflow: hidden; }
  body {
    position: relative;
    background: var(--board);
    font-family: "Exo 2", "Helvetica Neue", Arial, sans-serif;
    color: var(--ink);
  }
  .piece { position: absolute; background: var(--paper); box-shadow: var(--shadow); overflow: hidden; }

  /* Brand mark stand-in */
  .brand { position: absolute; display: flex; flex-direction: column; align-items: center; text-align: center; }
  .brand-dot { border-radius: 50%; background: var(--logo-blue); }
  .brand-name {
    font-weight: 700; color: var(--logo-blue);
    text-transform: uppercase; line-height: 1.1; letter-spacing: 0.04em;
  }

  /* Fine accent rules */
  .rule-v {
    position: absolute; width: 2px;
    background: linear-gradient(to bottom, rgba(27,127,208,0) 0%, var(--accent-light) 35%, var(--accent) 100%);
  }
  .rule-h {
    position: absolute; height: 2px;
    background: linear-gradient(to right, rgba(27,127,208,0) 0%, var(--accent-light) 40%, var(--accent) 100%);
  }

  /* Letterhead */
  .letterhead { left: 72px; top: 124px; width: 501px; height: 706px; }
  .letterhead .rule-v { left: 476px; top: 0; height: 682px; }
  .letterhead .rule-h { left: 0; top: 680px; width: 478px; }
  .letterhead .brand { left: 333px; top: 40px; width: 101px; }
  .letterhead .brand-dot { width: 34px; height: 34px; margin-bottom: 10px; }
  .letterhead .brand-name { font-size: 9px; }
  .letterhead-contact { position: absolute; right: 67px; top: 561px; text-align: right; font-style: normal; }
  .contact-venue { font-size: 10.5px; font-weight: 600; margin-bottom: 9px; }
  .contact-line { font-size: 7px; line-height: 9px; color: var(--ink-soft); }
  .contact-phone { font-size: 7px; margin-top: 10px; color: var(--ink-soft); }
  .contact-web { font-size: 9px; margin-top: 11px; letter-spacing: 0.02em; }

  /* Business cards */
  .card { width: 219px; height: 128px; }
  .card-front { left: 653px; top: 123px; }
  .card-front .brand { left: 0; top: 26px; width: 219px; }
  .card-front .brand-dot { width: 48px; height: 48px; margin-bottom: 9px; }
  .card-front .brand-name { font-size: 9px; }
  .card-front .rule-h { left: 0; bottom: 0; width: 219px; }

  .card-back { left: 905px; top: 123px; }
  .card-back .rule-v { left: 100px; top: 0; height: 128px; }
  .card-back .brand { left: 6px; top: 50px; width: 50px; }
  .card-back .brand-dot { width: 18px; height: 18px; margin-bottom: 4px; }
  .card-back .brand-name { font-size: 4.5px; }
  .card-details { position: absolute; right: 14px; top: 19px; text-align: right; font-size: 6.5px; line-height: 8.2px; color: var(--ink-soft); }
  .card-details .person { font-weight: 600; color: var(--ink); }
  .card-details .gap { margin-top: 13px; }
  .card-details .web { margin-top: 8px; font-weight: 600; color: var(--ink); }

  /* Compliment card */
  .compliment { left: 444px; top: 346px; width: 524px; height: 260px; }
  .compliment .rule-v { left: 244px; top: 0; height: 260px; }
  .compliment .brand { left: 20px; top: 70px; width: 132px; }
  .compliment .brand-dot { width: 70px; height: 70px; margin-bottom: 8px; }
  .compliment .brand-name { font-size: 12px; }

  /* Envelope */
  .envelope { left: 611px; top: 638px; width: 523px; height: 262px; }
  .envelope-flap { position: absolute; left: 0; top: 0; width: 523px; height: 110px; }
  .envelope .rule-h { left: 0; bottom: 0; width: 523px; }
  .envelope .brand { left: 414px; top: 176px; width: 74px; }
  .envelope .brand-dot { width: 32px; height: 32px; margin-bottom: 4px; }
  .envelope .brand-name { font-size: 6.5px; }
</style>
</head>
<body>

  <!-- Letterhead -->
  <section class="piece letterhead" aria-label="Letterhead">
    <div class="rule-v"></div>
    <div class="rule-h"></div>
    <div class="brand">
      <span class="brand-dot"></span>
      <span class="brand-name">Gold Lantern Pictures</span>
    </div>
    <address class="letterhead-contact">
      <p class="contact-venue">Ridgeway Studio Park</p>
      <p class="contact-line">2850 Halverson Street | Tower Annex, 4th Floor</p>
      <p class="contact-line">Manhattan Beach, CA 90412</p>
      <p class="contact-phone">310-555-0148 : Phone</p>
      <p class="contact-web">www.goldlanternpicturesco.example</p>
    </address>
  </section>

  <!-- Business card front -->
  <section class="piece card card-front" aria-label="Business card front">
    <div class="brand">
      <span class="brand-dot"></span>
      <span class="brand-name">Gold Lantern Pictures</span>
    </div>
    <div class="rule-h"></div>
  </section>

  <!-- Business card back -->
  <section class="piece card card-back" aria-label="Business card back">
    <div class="rule-v"></div>
    <div class="brand">
      <span class="brand-dot"></span>
      <span class="brand-name">Gold Lantern Pictures</span>
    </div>
    <div class="card-details">
      <p class="person">Jane Marlow</p>
      <p class="person">Director</p>
      <p>jane@goldlanternpicturesco.example</p>
      <p class="person gap">Ridgeway Studio Park</p>
      <p>2850 Halverson Street</p>
      <p>Tower Annex, 4th Floor</p>
      <p>Manhattan Beach, CA 90412</p>
      <p>Phone: 310-555-0148</p>
      <p class="web">www.goldlanternpicturesco.example</p>
    </div>
  </section>

  <!-- Compliment card -->
  <section class="piece compliment" aria-label="Compliment card">
    <div class="rule-v"></div>
    <div class="brand">
      <span class="brand-dot"></span>
      <span class="brand-name">Gold Lantern Pictures</span>
    </div>
  </section>

  <!-- Envelope -->
  <section class="piece envelope" aria-label="Envelope">
    <svg class="envelope-flap" width="523" height="110" viewBox="0 0 523 110" aria-hidden="true">
      <defs>
        <linearGradient id="flap-line" x1="0" y1="0" x2="1" y2="0">
          <stop offset="0" stop-color="#d9dde3"/>
          <stop offset="0.6" stop-color="#a9c6ea"/>
          <stop offset="1" stop-color="#1b7fd0"/>
        </linearGradient>
      </defs>
      <polyline points="0,0 25,100 523,100" fill="none" stroke="url(#flap-line)" stroke-width="1.2"/>
    </svg>
    <div class="rule-h"></div>
    <div class="brand">
      <span class="brand-dot"></span>
      <span class="brand-name">Gold Lantern Pictures</span>
    </div>
  </section>

</body>
</html>
```